Business Card Design

​Silver Harbor Rhythms provides personal, friendly service in a fun and high energy environment. We are based in Vermont.

We would like a card that appeals to a wide range of audiences as we do a wide range of events. Please feel free to check out our website silverharborrhythms.com for inspiration.

Target Market(s)

weddings, corporate, birthday parties, colleges

Industry/Entity Type

Business

Contact Information for Business Card

Silver Harbor Rhythms
Providing Entertainment For All Occasions
555 014 2968
silverharborrhythms@mailquill.net
silverharborrhythms.com

```html
<!DOCTYPE html>
<html lang="en">
<head>
<meta charset="utf-8">
<title>Silver Harbor Rhythms – Business Card</title>
<link rel="stylesheet" href="https://fonts.googleapis.com/css2?family=Questrial&family=Cormorant+SC:wght@600&display=swap">
<style>
  :root {
    --stage: #e9e9ea;
    --card-white: #ffffff;
    --card-black: #0c0c0d;
    --brand-green: #2f6b2a;
    --soft-green: #6f9a5e;
    --accent-red: #c8303a;
    --deep-red: #6e1f25;
    --ink: #222224;
  }
  * { box-sizing: border-box; margin: 0; padding: 0; }
  html, body { width: 1200px; height: 871px; overflow: hidden; }
  body {
    background: var(--stage);
    display: flex;
    flex-direction: column;
    align-items: center;
    justify-content: center;
    gap: 44px;
    font-family: "Questrial", "Century Gothic", sans-serif;
  }
  .card {
    position: relative;
    width: 620px;
    height: 354px;
    overflow: hidden;
    box-shadow: 0 6px 18px rgba(0,0,0,0.18);
  }
  .card--back {
    background: var(--card-black);
    display: flex;
    align-items: center;
    justify-content: center;
  }
  .card--front { background: var(--card-white); }

  .wordmark {
    color: var(--brand-green);
    font-family: "Questrial", "Century Gothic", sans-serif;
    text-transform: uppercase;
    letter-spacing: 0.04em;
    display: flex;
    align-items: center;
    gap: 10px;
  }
  .wordmark__dot {
    width: 12px; height: 12px;
    border-radius: 50%;
    background: var(--brand-green);
  }
  .card--back .wordmark { font-size: 30px; }
  .card--front .wordmark {
    position: absolute;
    left: 40px; top: 46px;
    font-size: 19px;
  }

  .person {
    position: absolute;
    left: 40px; top: 118px;
  }
  .person__name {
    font-family: "Cormorant SC", Georgia, serif;
    font-weight: 600;
    font-size: 17px;
    color: var(--brand-green);
    letter-spacing: 0.03em;
  }
  .person__role {
    margin-top: 4px;
    font-size: 10px;
    color: var(--accent-red);
  }

  .contact {
    position: absolute;
    left: 40px; top: 196px;
    list-style: none;
    display: flex;
    flex-direction: column;
    gap: 11px;
  }
  .contact__item {
    display: flex;
    align-items: center;
    gap: 14px;
    font-size: 12px;
    color: var(--ink);
    letter-spacing: 0.02em;
  }
  .contact__icon { width: 14px; height: 14px; flex: none; }

  .backdrop {
    position: absolute;
    right: 0; bottom: 0;
    width: 330px; height: 250px;
    background:
      linear-gradient(to top, rgba(111,154,94,0.55) 0%, rgba(111,154,94,0.15) 45%, rgba(255,255,255,0) 70%),
      linear-gradient(to left, rgba(200,48,58,0.28) 0%, rgba(200,48,58,0.08) 55%, rgba(255,255,255,0) 100%);
    -webkit-mask-image: linear-gradient(to right, transparent 0%, #000 40%);
            mask-image: linear-gradient(to right, transparent 0%, #000 40%);
  }
</style>
</head>
<body>

  <section class="card card--back" aria-label="Card back">
    <div class="wordmark"><span class="wordmark__dot"></span>Silver Harbor Rhythms</div>
  </section>

  <section class="card card--front" aria-label="Card front">
    <div class="wordmark"><span class="wordmark__dot"></span>Silver Harbor Rhythms</div>

    <div class="person">
      <p class="person__name">Mara Quinlan</p>
      <p class="person__role">CEO</p>
    </div>

    <ul class="contact">
      <li class="contact__item">
        <svg class="contact__icon" viewBox="0 0 14 14" aria-hidden="true">
          <path d="M2 5 Q7 1 12 5 L11 7 L9 6 L9 5 Q7 4 5 5 L5 6 L3 7 Z" fill="var(--brand-green)"/>
          <rect x="3" y="8" width="8" height="4" rx="1" fill="none" stroke="var(--brand-green)" stroke-width="1.2"/>
        </svg>
        555 014 2968
      </li>
      <li class="contact__item">
        <svg class="contact__icon" viewBox="0 0 14 14" aria-hidden="true">
          <rect x="1" y="3" width="12" height="8" fill="none" stroke="var(--brand-green)" stroke-width="1.3"/>
          <path d="M1 3 L7 8 L13 3" fill="none" stroke="var(--brand-green)" stroke-width="1.3"/>
        </svg>
        silverharborrhythms@mailquill.net
      </li>
      <li class="contact__item">
        <svg class="contact__icon" viewBox="0 0 14 14" aria-hidden="true">
          <circle cx="7" cy="7" r="5.5" fill="none" stroke="var(--brand-green)" stroke-width="1.3"/>
          <ellipse cx="7" cy="7" rx="2.3" ry="5.5" fill="none" stroke="var(--brand-green)" stroke-width="1"/>
          <line x1="1.5" y1="7" x2="12.5" y2="7" stroke="var(--brand-green)" stroke-width="1"/>
        </svg>
        silverharborrhythms.com
      </li>
    </ul>

    <div class="backdrop" role="img" aria-label="Faint decorative backdrop area in soft green and red tones"></div>
  </section>

</body>
</html>
```